Website for premium health insurance and concierge medicine

This is a brand new website for Brask Insurance Services that specializes in Health Insurance and Concierge Medicine for high net-worth and affluent individuals and families. Through this website, clients will be able to learn about products and services, submit applications, and complete self enrollment forms. The website needs to have a premium look & feel that will appeal to a discerning high net-worth individual.

I’m looking for 4 pages in total to begin with. I’m also looking for a designer who will be interested in continuing to build out this new site further over the next few months.

The headline for each page is listed below:

Page 1: HOME PAGE
“Premium Healthcare | Bespoke Concierge Services | Absolute Peace of Mind.”

Page 2: HEALTH INSURANCE
“Premium Healthcare | Elevated.”

Page 3: CONCIERGE MEDICINE
“Personalized Medicine | At-Home Concierge Care | Your Private Physician, 24/7.”

Page 4: DENTAL & VISION
“Your Smile | Your Vision | Perfected.”

Here are several links to existing websites that can be used as design inspiration:

https://vantromhealth.com
https://www.pelvix.org/specialties-services/other-programs-services/concierge-medicine
https://wardelmdnx.com

More generally speaking, I like a clean, modern, dutch style of websites. Here’s an unrelated site that has a good design:

https://www.morvathis.com

Here are a few additional phrases and keywords that will help inspire the design:

Premium Health Insurance
Executive Health Insurance
Concierge Medicine
24/7 access dedicated concierge team
Integrative Concierge Care

I will upload logo files below, here are the font & colors information:

Font: Trajan Pro Bold
Colors:
Blue: hex code: 0071BD, Rgb code: 0, 113, 189  cmyk code: 87,53,0,0
Gray: hex code: #666666, Rgb code: 102,102,102 cmyk code: 60,51,51,20

```html
<!DOCTYPE html>
<html lang="en">
<head>
<meta charset="utf-8">
<title>Brask Insurance Services</title>
<link href="https://fonts.googleapis.com/css2?family=Tinos:wght@400;700&family=Open+Sans:wght@400;600;700&family=Roboto:wght@400;500;700&display=swap" rel="stylesheet">
<style>
:root{
  --blue:#0b6cbf;
  --blue-bright:#2f8fe0;
  --navy:#1b2a4e;
  --navy-deep:#1a2342;
  --ink:#1d2a48;
  --gray:#666666;
  --muted:#8a8f99;
  --light:#eef3f8;
  --white:#ffffff;
  --serif:'Tinos',serif;
  --sans:'Open Sans',sans-serif;
  --ui:'Roboto',sans-serif;
}
*{box-sizing:border-box;margin:0;padding:0}
html,body{width:1200px;height:4612px;overflow:hidden}
body{position:relative;background:var(--white);font-family:var(--sans);color:var(--gray)}
.abs{position:absolute}
.topbar{left:0;top:0;width:1200px;height:40px;background:var(--white);font-size:11px;font-weight:600;color:var(--ink)}
.topbar .item{position:absolute;top:13px;display:flex;align-items:center;gap:8px}
.topbar .sep{position:absolute;top:11px;width:1px;height:18px;background:#9aa3b5}
.socials{position:absolute;right:118px;top:14px;display:flex;gap:16px}
.socials span{width:10px;height:10px;border-radius:50%;background:#8a97b3}
.header{left:0;top:40px;width:1200px;height:121px;background:var(--navy)}
.brand-mark{display:flex;align-items:center;gap:10px;font-family:var(--serif);color:#fff;font-size:15px;font-weight:700;line-height:1.1}
.brand-mark .dot{width:30px;height:30px;border-radius:50%;background:var(--blue)}
.perk{position:absolute;top:28px;display:flex;align-items:center;gap:12px;color:#fff;font-size:12px;font-weight:700;line-height:1.35}
.perk .ring{width:24px;height:24px;border:2px solid var(--blue-bright);border-radius:50%}
.nav{left:91px;top:125px;width:994px;height:68px;background:#fff;box-shadow:0 4px 14px rgba(0,0,0,.15);display:block}
.nav a{position:absolute;top:24px;font-size:14px;color:var(--ink);text-decoration:none;font-weight:500;font-family:var(--ui)}
.nav .active::after{content:"";position:absolute;left:-24px;right:-24px;top:41px;height:3px;background:var(--blue)}
.quote-btn{position:absolute;left:817px;top:16px;width:152px;height:38px;border-radius:19px;background:var(--blue-bright);color:#fff;font-size:13px;font-weight:700;display:flex;align-items:center;justify-content:center;font-family:var(--ui)}
.hero-photo{left:0;top:161px;width:1200px;height:680px;background:linear-gradient(160deg,#b9bec5 0%,#7d8591 45%,#4d5564 100%)}
.hero-title{left:235px;top:385px;width:729px;height:84px;background:var(--blue);color:#fff;font-family:var(--serif);font-size:50px;display:flex;align-items:center;justify-content:center}
.hero-sub{left:161px;top:475px;width:878px;height:71px;background:rgba(20,22,28,.85);color:#fff;font-size:19px;font-weight:600;text-align:center;line-height:1.35;display:flex;align-items:center;justify-content:center;padding:0 20px}
.eyebrow{font-size:12px;font-weight:600;color:var(--blue);text-transform:uppercase;text-decoration:underline;text-underline-offset:4px}
.eyebrow.light{color:#fff}
.h2{font-family:var(--serif);font-weight:700;color:var(--ink);font-size:46px}
.btn{display:flex;align-items:center;justify-content:center;gap:14px;background:var(--blue);color:#fff;font-weight:700;font-size:15px;font-family:var(--ui);box-shadow:0 3px 8px rgba(0,0,0,.2)}
.about-emblem{left:150px;top:955px;width:380px;height:410px;display:flex;align-items:center;justify-content:center;flex-direction:column;gap:24px}
.about-emblem .circle{width:240px;height:240px;border-radius:50%;border:14px solid var(--blue)}
.about-emblem .name{font-family:var(--serif);font-weight:700;font-size:26px;color:var(--blue)}
.about-copy{left:630px;top:952px;width:510px}
.about-copy h2{font-size:43px;line-height:1.25;margin-top:20px}
.about-copy .lead{font-family:var(--serif);font-size:25px;color:var(--ink);margin-top:22px}
.about-copy p.body{font-size:13px;line-height:1.65;margin-top:14px}
.services-bg{left:0;top:1640px;width:1200px;height:554px;background:var(--light)}
.center{left:0;width:1200px;text-align:center}
.card{top:1760px;width:304px;height:255px;background:#fff;box-shadow:0 3px 12px rgba(0,0,0,.1);text-align:center}
.card .img{position:absolute;left:16px;top:15px;width:272px;height:154px;background:linear-gradient(135deg,#5a5f66,#a7a49c 55%,#3e4148)}
.card .badge{position:absolute;right:16px;top:130px;width:58px;height:58px;border-radius:50%;background:var(--blue);border:4px solid #fff;display:flex;align-items:center;justify-content:center}
.card .tag{position:absolute;left:0;right:0;top:191px;font-size:11px;font-weight:700;color:var(--blue)}
.card h3{position:absolute;left:0;right:0;top:212px;font-family:var(--serif);font-size:20px;color:var(--ink)}
.why{left:0;top:2194px;width:1200px;height:424px;background:linear-gradient(180deg,#26335a 0%,#1f2c52 100%)}
.why-item .circle{position:absolute;width:96px;height:96px;border-radius:50%;background:#fff;border:6px solid var(--blue);display:flex;align-items:center;justify-content:center}
.why-item .box{position:absolute;width:215px;height:121px;border:2px dashed #fff;padding:14px 24px;color:#fff}
.why-item .box h4{font-family:var(--serif);font-size:18px}
.why-item .box p{font-size:11px;line-height:1.3;margin-top:6px}
.why-item .node{position:absolute;width:16px;height:16px;border-radius:50%;background:var(--blue);border:2px dotted #fff}
.review .photo{position:absolute;width:89px;height:122px;background:linear-gradient(180deg,#d9d7d3,#9aa0a8)}
.review .name{position:absolute;font-size:18px;font-weight:600;color:var(--ink)}
.review .role{position:absolute;font-size:12px;color:var(--muted)}
.review .quote{position:absolute;font-family:var(--serif);font-size:70px;font-weight:700;color:var(--blue);line-height:1}
.review .card-r{position:absolute;width:303px;height:147px;background:#fff;box-shadow:0 3px 12px rgba(0,0,0,.1);padding:20px 32px;font-size:13px;line-height:1.9;color:var(--muted)}
.contact-left{left:141px;top:3478px;width:380px}
.contact-left h3{font-family:var(--ui);font-weight:700;font-size:32px;color:var(--ink);line-height:1.2}
.contact-left h3 span{display:block;color:var(--blue-bright);font-weight:400}
.contact-left p{font-size:12px;line-height:1.9;margin-top:16px;color:var(--muted)}
.contact-left hr{border:0;border-top:1px solid #cfd4dc;margin-top:26px}
.c-line{position:absolute;left:54px;font-size:13px;color:var(--muted);display:flex;align-items:center;gap:22px}
.form-card{left:591px;top:3421px;width:484px;height:4px;border-top:3px solid var(--blue);border-radius:6px 6px 0 0}
.f-label{position:absolute;font-size:13px;font-weight:700;color:var(--blue);font-family:var(--ui)}
.f-input{position:absolute;border:1px solid #b9c0cc;font-size:11px;color:var(--muted);padding:14px 18px;background:#fff}
.submit{left:620px;top:3870px;width:125px;height:40px;background:var(--blue);color:#fff;font-size:13px;font-weight:700;display:flex;align-items:center;justify-content:center;font-family:var(--ui)}
.footer{left:0;top:4040px;width:1200px;height:534px;background:var(--navy-deep);color:#fff}
.f-head{position:absolute;font-family:var(--ui);font-size:22px;font-weight:700;color:#fff}
.f-link{position:absolute;font-size:14px;color:#fff;display:flex;align-items:center;gap:14px}
.info-bar{left:84px;top:4472px;width:1026px;height:84px;background:#2b3556;color:#fff}
.info-bar .it{position:absolute;top:20px;display:flex;gap:22px;align-items:center}
.info-bar b{display:block;font-size:14px}
.info-bar small{font-size:15px}
.bottom-strip{left:0;top:4574px;width:1200px;height:38px;background:#fff;font-size:13px;color:var(--ink)}
.to-top{left:1125px;top:4528px;width:48px;height:48px;background:var(--blue);display:flex;align-items:center;justify-content:center}
</style>
</head>
<body>

<!-- Top bar -->
<div class="abs topbar">
  <div class="item" style="left:88px">
    <svg width="12" height="12" viewBox="0 0 24 24"><path d="M6.6 10.8a15 15 0 0 0 6.6 6.6l2.2-2.2c.3-.3.7-.4 1-.2 1.1.4 2.3.6 3.6.6.6 0 1 .4 1 1V20c0 .6-.4 1-1 1A17 17 0 0 1 3 4c0-.6.4-1 1-1h3.5c.6 0 1 .4 1 1 0 1.3.2 2.5.6 3.6.1.3 0 .7-.2 1z" fill="#0b6cbf"/></svg>
    (614) 208-3391
  </div>
  <div class="sep" style="left:238px"></div>
  <div class="item" style="left:254px">
    <svg width="13" height="10" viewBox="0 0 24 18"><rect width="24" height="18" rx="2" fill="#0b6cbf"/><path d="M1 2l11 8 11-8" stroke="#fff" stroke-width="2" fill="none"/></svg>
    hello@braskinsure.com
  </div>
  <div class="sep" style="left:410px"></div>
  <div class="item" style="left:426px">
    <svg width="10" height="13" viewBox="0 0 20 26"><path d="M10 0a10 10 0 0 0-10 10c0 7 10 16 10 16s10-9 10-16A10 10 0 0 0 10 0z" fill="#0b6cbf"/><circle cx="10" cy="10" r="4" fill="#fff"/></svg>
    48 Harlow Lane
  </div>
  <div class="socials"><span></span><span></span><span></span><span></span></div>
</div>

<!-- Header -->
<div class="abs header">
  <div class="brand-mark" style="position:absolute;left:106px;top:16px"><span class="dot"></span>Brask Insurance<br>Services</div>
  <div class="perk" style="left:806px"><span class="ring"></span><span>24/7<br>Service</span></div>
  <div style="position:absolute;left:938px;top:24px;width:2px;height:40px;background:#fff"></div>
  <div class="perk" style="left:966px"><span class="ring"></span><span>Qualified<br>Professionals</span></div>
</div>

<!-- Hero -->
<div class="abs hero-photo" role="img" aria-label="Photo of business people walking across an office atrium seen from above"></div>
<svg class="abs" style="left:0;top:161px" width="1200" height="700" viewBox="0 0 1200 700">
  <path d="M0 502 Q 600 700 1200 573 L1200 700 L0 700 Z" fill="#0b6cbf"/>
  <path d="M0 548 Q 560 735 1200 610 L1200 700 L0 700 Z" fill="#ffffff"/>
</svg>

<nav class="abs nav">
  <a class="active" style="left:56px">Home</a>
  <a style="left:198px">About Us</a>
  <a style="left:335px">Services</a>
  <a style="left:482px">Our Team</a>
  <a style="left:622px">Contact Us</a>
  <div class="quote-btn">Get A Quote</div>
</nav>

<div class="abs hero-title">Health insurance simplified.</div>
<div class="abs hero-sub">Lorem ipsum dolor sit amet, consectetur adipiscing elit, sed do eiusmod tempor incididunt ut labore et dolore magna aliqua. Ut enim ad minim</div>

<!-- About -->
<div class="abs about-emblem">
  <div class="circle"></div>
  <div class="name">Brask Insurance Services</div>
</div>
<div class="abs about-copy">
  <div class="eyebrow">Who we are</div>
  <h2 class="h2">Reliable coverage, for<br>a healthier you.</h2>
  <div class="lead">Affordable health, accessible care.</div>
  <p class="body">Lorem ipsum dolor sit amet, consectetur adipiscing elit, sed do eiusmod tempor incididunt ut labore et dolore magna aliqua. Ut enim ad minim veniam, quis nos trud exercitation ullamco laboris nisi ut aliquip ex ea commodo consequat.<br>Duis aute irure dolor in reprehenderit in voluptate velit esse cillum dolore eu fugiat nulla pariatur. Excepteur sint occaecat cupidatat non proident, sunt in culpa qui officia deserunt mollit anim id est laborum.</p>
</div>
<div class="abs btn" style="left:629px;top:1325px;width:154px;height:43px">Contact us
  <svg width="16" height="12" viewBox="0 0 16 12"><path d="M0 6h14M9 1l5 5-5 5" stroke="#fff" stroke-width="2" fill="none"/></svg></div>

<!-- Services -->
<svg class="abs" style="left:0;top:1440px" width="1200" height="202" viewBox="0 0 1200 202">
  <path d="M0 109 C 200 10, 450 0, 1200 181 L1200 202 L0 202 Z" fill="#eef3f8"/>
  <path d="M0 109 C 200 10, 450 0, 1200 181" stroke="#0b6cbf" stroke-width="7" fill="none"/>
</svg>
<div class="abs services-bg"></div>
<div class="abs center" style="top:1624px"><span class="eyebrow">Our services</span></div>
<div class="abs center h2" style="top:1656px">Services We Offer</div>

<div class="abs card" style="left:122px">
  <div class="img" role="img" aria-label="Photo of an advisor meeting clients at a desk"></div>
  <div class="badge"><svg width="26" height="26" viewBox="0 0 24 24"><path d="M12 2l3 6.5 7 .8-5.2 4.8 1.4 7L12 17.6 5.8 21l1.4-7L2 9.3l7-.8z" stroke="#fff" stroke-width="1.6" fill="none"/></svg></div>
  <div class="tag">OUR SERVICES</div>
  <h3>Health Insurance</h3>
</div>
<div class="abs card" style="left:451px">
  <div class="img" role="img" aria-label="Photo of an advisor meeting clients at a desk"></div>
  <div class="badge"><svg width="26" height="26" viewBox="0 0 24 24"><path d="M12 2l3 6.5 7 .8-5.2 4.8 1.4 7L12 17.6 5.8 21l1.4-7L2 9.3l7-.8z" stroke="#fff" stroke-width="1.6" fill="none"/></svg></div>
  <div class="tag">OUR SERVICES</div>
  <h3>Concierge Medicine</h3>
</div>
<div class="abs card" style="left:781px">
  <div class="img" role="img" aria-label="Photo of an advisor meeting clients at a desk"></div>
  <div class="badge"><svg width="26" height="26" viewBox="0 0 24 24"><path d="M12 2l3 6.5 7 .8-5.2 4.8 1.4 7L12 17.6 5.8 21l1.4-7L2 9.3l7-.8z" stroke="#fff" stroke-width="1.6" fill="none"/></svg></div>
  <div class="tag">OUR SERVICES</div>
  <h3>Dental and Vision</h3>
</div>
<div class="abs btn" style="left:521px;top:2085px;width:154px;height:43px">Contact us
  <svg width="16" height="12" viewBox="0 0 16 12"><path d="M0 6h14M9 1l5 5-5 5" stroke="#fff" stroke-width="2" fill="none"/></svg></div>

<!-- Why choose us -->
<div class="abs why" role="img" aria-label="Dark blue tinted photo of a smiling team in an office"></div>
<div class="abs center" style="top:2270px"><span class="eyebrow light" style="color:#fff">Why choose us</span></div>
<div class="abs center h2" style="top:2300px;color:#fff">Why we are the Best</div>

<div class="why-item">
  <div class="circle" style="left:63px;top:2434px"><svg width="40" height="40" viewBox="0 0 24 24"><path d="M12 2l3 6.5 7 .8-5.2 4.8 1.4 7L12 17.6 5.8 21l1.4-7L2 9.3l7-.8z" stroke="#0b6cbf" stroke-width="1.4" fill="none"/></svg></div>
  <div class="node" style="left:175px;top:2474px"></div>
  <div class="box" style="left:183px;top:2420px"><h4>Professional</h4><p>Lorem ipsum dolor sit amet, consectetur adipiscing elit, sed do eiusmod tem Lorem ipsum dolor sdolor s</p></div>
</div>
<div class="why-item">
  <div class="circle" style="left:432px;top:2434px"><svg width="40" height="40" viewBox="0 0 24 24"><path d="M12 2l3 6.5 7 .8-5.2 4.8 1.4 7L12 17.6 5.8 21l1.4-7L2 9.3l7-.8z" stroke="#0b6cbf" stroke-width="1.4" fill="none"/></svg></div>
  <div class="node" style="left:544px;top:2474px"></div>
  <div class="box" style="left:552px;top:2420px"><h4>Client centric</h4><p>Lorem ipsum dolor sit amet, consectetur adipiscing elit, sed do eiusmod tem Lorem ipsum dolor sdolor s</p></div>
</div>
<div class="why-item">
  <div class="circle" style="left:801px;top:2434px"><svg width="40" height="40" viewBox="0 0 24 24"><path d="M12 2l3 6.5 7 .8-5.2 4.8 1.4 7L12 17.6 5.8 21l1.4-7L2 9.3l7-.8z" stroke="#0b6cbf" stroke-width="1.4" fill="none"/></svg></div>
  <div class="node" style="left:913px;top:2474px"></div>
  <div class="box" style="left:921px;top:2420px"><h4>Experienced</h4><p>Lorem ipsum dolor sit amet, consectetur adipiscing elit, sed do eiusmod tem Lorem ipsum dolor sdolor s</p></div>
</div>

<!-- Testimonials -->
<div class="abs center" style="top:2696px"><span class="eyebrow">Testimonials</span></div>
<div class="abs center h2" style="top:2728px">Clients Reviews</div>

<div class="review">
  <div class="photo" style="left:90px;top:2833px" role="img" aria-label="Portrait of a client"></div>
  <div class="name" style="left:202px;top:2854px">Martin Oberlay</div>
  <div class="role" style="left:204px;top:2884px">CEO &amp; Founder</div>
  <div class="quote" style="left:356px;top:2928px">&rdquo;</div>
  <div class="card-r" style="left:111px;top:2955px">Lorem ipsum dolor sit amet, consect etur adipiscing elit, sed do eiusmod tempor incididunt ut labore et dolore magna aliqua. Ut enim ad minim veni am, quis nostrud</div>
</div>
<div class="review">
  <div class="photo" style="left:439px;top:2833px" role="img" aria-label="Portrait of a client"></div>
  <div class="name" style="left:544px;top:2854px">Martin Oberlay</div>
  <div class="role" style="left:546px;top:2884px">CEO &amp; Founder</div>
  <div class="quote" style="left:705px;top:2928px">&rdquo;</div>
  <div class="card-r" style="left:460px;top:2955px">Lorem ipsum dolor sit amet, consect etur adipiscing elit, sed do eiusmod tempor incididunt ut labore et dolore magna aliqua. Ut enim ad minim veni am, quis nostrud</div>
</div>
<div class="review">
  <div class="photo" style="left:788px;top:2833px" role="img" aria-label="Portrait of a client"></div>
  <div class="name" style="left:886px;top:2854px">Martin Oberlay</div>
  <div class="role" style="left:888px;top:2884px">CEO &amp; Founder</div>
  <div class="quote" style="left:1054px;top:2928px">&rdquo;</div>
  <div class="card-r" style="left:809px;top:2955px">Lorem ipsum dolor sit amet, consect etur adipiscing elit, sed do eiusmod tempor incididunt ut labore et dolore magna aliqua. Ut enim ad minim veni am, quis nostrud</div>
</div>

<svg class="abs" style="left:0;top:3130px" width="1200" height="190" viewBox="0 0 1200 190">
  <path d="M0 22 Q 600 262 1200 94 L1200 80 Q 600 240 0 22 Z" fill="#0b6cbf"/>
</svg>
<div class="abs btn" style="left:521px;top:3177px;width:154px;height:43px">Contact us
  <svg width="16" height="12" viewBox="0 0 16 12"><path d="M0 6h14M9 1l5 5-5 5" stroke="#fff" stroke-width="2" fill="none"/></svg></div>

<!-- Contact -->
<div class="abs contact-left">
  <h3>Get&nbsp; in Touch<span>Contact Us</span></h3>
  <p>Lorem ipsum dolor sit amet, consectetur adipiscing e lit, sed do eiusmod tempor incididunt ut labore et dolore magna aliqua. ceptos ...</p>
  <hr>
</div>
<div class="c-line abs" style="left:150px;top:3728px">
  <svg width="14" height="16" viewBox="0 0 20 26"><path d="M10 0a10 10 0 0 0-10 10c0 7 10 16 10 16s10-9 10-16A10 10 0 0 0 10 0z" fill="#0b6cbf"/><circle cx="10" cy="10" r="4" fill="#fff"/></svg>
  Kestrelweg 9, 4720 Lindhaven</div>
<div class="c-line abs" style="left:150px;top:3791px">
  <svg width="14" height="14" viewBox="0 0 24 24"><path d="M6.6 10.8a15 15 0 0 0 6.6 6.6l2.2-2.2c.3-.3.7-.4 1-.2 1.1.4 2.3.6 3.6.6.6 0 1 .4 1 1V20c0 .6-.4 1-1 1A17 17 0 0 1 3 4c0-.6.4-1 1-1h3.5c.6 0 1 .4 1 1 0 1.3.2 2.5.6 3.6.1.3 0 .7-.2 1z" fill="#0b6cbf"/></svg>
  +41 2 7788103456</div>
<div class="c-line abs" style="left:150px;top:3846px">
  <svg width="14" height="11" viewBox="0 0 24 18"><rect width="24" height="18" rx="2" fill="#0b6cbf"/><path d="M1 2l11 8 11-8" stroke="#fff" stroke-width="2" fill="none"/></svg>
  desk@braskinsure.com</div>

<div class="abs form-card"></div>
<div class="f-label" style="left:625px;top:3468px">Full Name:</div>
<div class="f-input" style="left:620px;top:3501px;width:424px;height:43px">Sed non neque elit.</div>
<div class="f-label" style="left:625px;top:3572px">Email :</div>
<div class="f-label" style="left:851px;top:3572px">Phone no :</div>
<div class="f-input" style="left:620px;top:3603px;width:197px;height:43px">Sed non neque elit.</div>
<div class="f-input" style="left:849px;top:3603px;width:195px;height:43px">Sed non neque elit.</div>
<div class="f-label" style="left:625px;top:3683px">Messages :</div>
<div class="f-input" style="left:620px;top:3714px;width:424px;height:128px">Sed non neque elit.</div>
<div class="abs submit">SUBMIT</div>

<!-- Footer -->
<footer class="abs footer">
  <div class="brand-mark" style="position:absolute;left:84px;top:84px"><span class="dot"></span>Brask Insurance<br>Services</div>
  <div style="position:absolute;left:84px;top:166px;font-family:var(--ui);font-size:19px;font-weight:700">800-417-2290</div>
  <div style="position:absolute;left:86px;top:195px;font-size:14px;font-weight:700">Call for free consultation</div>
  <div style="position:absolute;left:86px;top:232px;width:300px;font-size:13px;line-height:1.7">Lorem ipsum dolor sit amet, consectet sed do eiusmod tempor incididunt ut la magna aliqua. Ut enim</div>
  <div style="position:absolute;left:86px;top:316px;font-size:14px;font-weight:700">Read more &nbsp;›</div>

  <div class="f-head" style="left:437px;top:88px">Useful Links</div>
  <div class="f-link" style="left:442px;top:164px">›<span>About Company</span></div>
  <div class="f-link" style="left:442px;top:195px">›<span>Leadership</span></div>
  <div class="f-link" style="left:442px;top:225px">›<span>Blog Post</span></div>
  <div class="f-link" style="left:442px;top:255px">›<span>FAQ'S</span></div>
  <div class="f-link" style="left:442px;top:286px">›<span>Certification</span></div>
  <div class="f-link" style="left:442px;top:316px">›<span>Testimonials</span></div>
  <div class="f-link" style="left:607px;top:164px">›<span>Services</span></div>
  <div class="f-link" style="left:607px;top:195px">›<span>Industries</span></div>
  <div class="f-link" style="left:607px;top:225px">›<span>Feedback</span></div>
  <div class="f-link" style="left:607px;top:255px">›<span>Partners</span></div>
  <div class="f-link" style="left:607px;top:286px">›<span>Pricing</span></div>
  <div class="f-link" style="left:607px;top:316px">›<span>Contct</span></div>

  <div class="f-head" style="left:788px;top:88px">Newsletter</div>
  <div style="position:absolute;left:786px;top:182px;width:320px;font-size:12px;font-weight:600;line-height:1.9">Dont miss to subscribe to our news feeds. kindly fill the form below</div>
  <div style="position:absolute;left:788px;top:257px;width:269px;height:46px;background:#28324f;border-radius:23px 0 0 23px;font-size:13px;font-weight:600;padding:14px 24px">Your Email Address</div>
  <div style="position:absolute;left:1057px;top:257px;width:50px;height:46px;background:var(--blue);border-radius:0 23px 23px 0;display:flex;align-items:center;justify-content:center">
    <svg width="12" height="18" viewBox="0 0 12 18"><path d="M2 2l7 7-7 7" stroke="#fff" stroke-width="2.5" fill="none"/></svg></div>
</footer>

<div class="abs info-bar">
  <div class="it" style="left:22px">
    <svg width="28" height="34" viewBox="0 0 20 26"><path d="M10 1a9 9 0 0 0-9 9c0 6.5 9 15 9 15s9-8.5 9-15a9 9 0 0 0-9-9z" stroke="#2f8fe0" stroke-width="1.5" fill="none"/><circle cx="10" cy="10" r="3.5" stroke="#2f8fe0" stroke-width="1.5" fill="none"/></svg>
    <div><b>Location</b><small>57 Crane Ave, NY 10418</small></div></div>
  <div style="position:absolute;left:342px;top:14px;width:1px;height:56px;background:#4a5475"></div>
  <div class="it" style="left:374px">
    <svg width="30" height="26" viewBox="0 0 30 26"><rect x="1" y="1" width="28" height="20" rx="3" stroke="#2f8fe0" stroke-width="1.6" fill="none"/><path d="M7 8h16M7 13h10" stroke="#2f8fe0" stroke-width="1.6"/><path d="M8 21l-2 4 6-4" stroke="#2f8fe0" stroke-width="1.6" fill="none"/></svg>
    <div><b>Mail us</b><small>support@braskinsure.com</small></div></div>
  <div style="position:absolute;left:686px;top:14px;width:1px;height:56px;background:#4a5475"></div>
  <div class="it" style="left:715px">
    <svg width="30" height="30" viewBox="0 0 30 30"><path d="M28 2L2 13l10 4 4 11z" stroke="#2f8fe0" stroke-width="1.6" fill="none"/><path d="M12 17l16-15" stroke="#2f8fe0" stroke-width="1.6"/></svg>
    <div><b>Office hrs</b><small>9.00am to 7.00pm (Mon-Sat)</small></div></div>
</div>

<div class="abs bottom-strip">
  <span style="position:absolute;left:86px;top:10px;font-weight:600">Brask Insurance Services</span>
  <span style="position:absolute;left:800px;top:10px">Privacy Policy</span>
  <span style="position:absolute;left:910px;top:10px">Terms &amp; Conditions</span>
  <span style="position:absolute;left:1053px;top:10px">Site Map</span>
</div>
<div class="abs to-top"><svg width="18" height="12" viewBox="0 0 18 12"><path d="M2 10l7-7 7 7" stroke="#fff" stroke-width="2.5" fill="none"/></svg></div>

</body>
</html>
```